Bridal Pastry Trade Institute Website Homepage Revision

I need the "homepage" to the new Coastal Bridal Pastry Trade Institute to reworked. The current homepage is dull. It needs the attention of a professional graphic artist so it delivers a professionally finished feel and look. I have included the current URL for your viewing (builds.vornelt.com/coastal-pastry/cms/ ) to see where we are in the development phase. The elements on the homepage are all necessary and the colors are correct. I have also included the original Word document for the page (you can extract the RGB values and images from the doc). To be clear, I am not looking to recreate all the web pages, just the homepage. It needs to be responsive and stretched.

Target Market(s)

All bakers who sell wedding cakes in the United States

Number of Pages Required

1 page

Font styles to use
Other font styles liked:
• see the Word Document

Requirements
Must have
• It must have the elements already in the original mock up. That includes the colors and fonts.

```html
<!DOCTYPE html>
<html lang="en">
<head>
<meta charset="utf-8">
<title>Coastal Bridal Pastry Trade Institute</title>
<link href="https://fonts.googleapis.com/css2?family=Open+Sans:wght@400;600;700&display=swap" rel="stylesheet">
<style>
:root{
  --teal:#1fc6c2;
  --pink:#d41a6c;
  --pink-light:#ef5ba0;
  --orange:#f7931e;
  --ink:#3a3a3a;
  --grey:#6a6a6a;
  --panel:#ededed;
  --footer:#1c1c1c;
  --white:#ffffff;
}
*{box-sizing:border-box;margin:0;padding:0}
html,body{width:1200px;height:3905px;overflow:hidden}
body{font-family:"Open Sans",Arial,sans-serif;color:var(--ink);background:var(--white);position:relative}
section,header,footer,nav{position:absolute;left:0;width:1200px}
.abs{position:absolute}

.main-nav{top:0;height:46px;background:var(--pink);display:flex;align-items:center;padding-left:88px}
.main-nav a{color:var(--white);font-size:13.5px;text-decoration:none;margin-right:32px;position:relative}
.main-nav a.active{font-weight:600}
.main-nav a.active::after{content:"";position:absolute;left:0;right:0;bottom:-13px;height:3px;background:var(--white)}

.hero{top:46px;height:527px}
.hero-copy{left:0;top:0;width:578px;height:527px;background:var(--teal)}
.brand{left:86px;top:22px;display:flex;align-items:center;gap:10px;color:var(--white);font-weight:700;font-size:14px;line-height:1.2;width:220px}
.brand-dot{width:22px;height:22px;border-radius:50%;background:var(--white);flex:none}
.hero-title{left:86px;top:172px;width:470px;color:var(--white);font-size:27px;line-height:36px;font-weight:700}
.field{position:absolute;background:var(--white);height:47px;font-size:12px;color:#555;padding:15px 12px}
.btn{position:absolute;background:var(--orange);color:var(--white);font-weight:600;text-align:center;font-size:17px}
.hero-photo{left:578px;top:0;width:622px;height:527px;background:linear-gradient(135deg,#e8eef2 0%,#cfd8de 45%,#f4f6f7 70%,#dfe7c8 100%)}

.press{top:573px;height:221px}
.press-title{top:40px;width:100%;text-align:center;color:var(--pink);font-size:16px}
.badge{position:absolute;top:83px;width:96px;height:94px;background:var(--white);box-shadow:0 1px 6px rgba(0,0,0,.25)}
.badge span{position:absolute;left:22px;top:28px;width:52px;height:38px;background:#c9c9c9;border-radius:4px}

.video-band{top:794px;height:450px;background:var(--panel)}
.video{left:302px;top:55px;width:598px;height:335px;background:#e9eef0;box-shadow:0 1px 4px rgba(0,0,0,.2);overflow:hidden}
.video-person{left:0;top:0;width:340px;height:305px;background:linear-gradient(160deg,#c7d3da,#7b95ad 55%,#4e6c8d)}
.video-quote{left:345px;top:70px;color:var(--pink);font-size:22px;font-weight:700}
.video-text{left:345px;top:108px;width:230px;color:#222;font-size:18px;line-height:26px;font-weight:600}
.video-bar{left:0;top:305px;width:598px;height:30px;background:#1d2a3a}

.research{top:1244px;height:404px}
.research-title{top:76px;width:100%;text-align:center;color:var(--pink);font-size:17px}
.path-card{position:absolute;top:128px;width:239px;height:200px;background:var(--teal);color:var(--white);text-align:center;box-shadow:0 2px 4px rgba(0,0,0,.15)}
.path-card svg{position:absolute;left:100px;top:18px}
.path-card p{position:absolute;top:82px;left:24px;right:24px;font-size:16.5px;line-height:22px}
.path-card .rule{position:absolute;left:0;right:0;top:142px;height:1px;background:rgba(255,255,255,.7)}
.path-card .cta{position:absolute;top:155px;left:0;right:0;font-weight:700;font-size:15px}

.offers{top:1648px;height:643px;background:radial-gradient(ellipse at 50% 40%,#f56fb0 0%,var(--pink-light) 35%,var(--pink) 100%)}
.offer{position:absolute;top:80px;width:326px;height:479px;background:var(--white)}
.offer .media{position:absolute;left:0;top:0;width:326px;height:266px}
.offer p{position:absolute;top:283px;left:20px;right:20px;text-align:center;font-size:17px;line-height:24px;color:#333}
.offer .btn{left:0;bottom:0;width:326px;height:47px;line-height:47px;font-weight:400}

.about{top:2291px;height:494px;background:var(--white);overflow:hidden}
.about-bg{right:0;top:0;width:820px;height:494px;background:linear-gradient(90deg,#fff 0%,rgba(248,232,236,.7) 40%,rgba(244,222,228,.6) 100%)}
.portrait-ring{left:130px;top:55px;width:238px;height:238px;border-radius:50%;border:6px solid var(--teal);background:var(--white);box-shadow:0 3px 8px rgba(0,0,0,.25)}
.portrait{left:8px;top:8px;width:210px;height:210px;border-radius:50%;background:radial-gradient(circle at 50% 45%,#f0c7a8,#c9966f 55%,#6d87a8 100%)}
.about-copy{left:463px;top:72px;width:580px}
.about-copy h2{color:var(--pink);font-size:17px;line-height:24px;font-weight:600;margin-bottom:18px}
.about-copy p{font-size:12.5px;line-height:19px;color:var(--grey);margin-bottom:16px}
.about-copy p.lead{color:#222;font-weight:700;margin-bottom:4px}

.insider{top:2785px;height:268px;background:var(--teal);overflow:hidden}
.insider-text{left:86px;top:22px;width:560px;color:var(--white);font-size:22px;line-height:33px}

.banner{top:3053px;height:461px;background:linear-gradient(180deg,#6b4a3f 0%,#8a6656 45%,#5a3d33 100%);display:flex;align-items:center;justify-content:center}
.banner-name{color:#e9d7c4;font-size:40px;font-weight:700;text-align:center}

.site-footer{top:3514px;height:391px;background:var(--footer);color:var(--white)}
.foot-col{position:absolute;top:68px}
.foot-col h3{font-size:16px;font-weight:700;margin-bottom:14px}
.foot-col li{list-style:none;font-size:12.5px;line-height:23px;color:#d8d8d8}
.foot-col li::before{content:"› "}
.foot-brand{left:877px;top:170px;display:flex;align-items:center;gap:8px;font-size:13px;font-weight:700;width:200px;line-height:1.2}
.foot-rule{left:86px;top:322px;width:1028px;height:1px;background:#3a3a3a}
.copyright{top:345px;width:100%;text-align:center;font-size:12px;color:#bdbdbd}
</style>
</head>
<body>

<nav class="main-nav">
  <a class="active">Home</a><a>Hal's Story</a><a>Marketing Solutions</a><a>Sales Solutions</a><a>Hire Us</a><a>Contact</a><a>Member Login</a><a>Partner with Us</a><a>Blog</a><a>My Courses</a>
</nav>

<header class="hero">
  <div class="hero-copy abs">
    <div class="brand abs"><span class="brand-dot"></span>Coastal Bridal Pastry Trade Institute</div>
    <h1 class="hero-title abs">Convince Brides to Choose You Even Before Their Consultation!</h1>
    <div class="field" style="left:86px;top:266px;width:198px">First Name</div>
    <div class="field" style="left:302px;top:266px;width:198px">Last Name</div>
    <div class="field" style="left:86px;top:334px;width:414px">Your Email</div>
    <div class="btn" style="left:86px;top:399px;width:203px;height:47px;line-height:47px">Subscribe Now</div>
  </div>
  <div class="hero-photo abs" role="img" aria-label="Photo of two pastry chefs in white jackets decorating a tiered wedding cake"></div>
</header>

<section class="press">
  <p class="press-title abs">Hal Brenner as Seen on</p>
  <div class="badge" style="left:86px"><span></span></div>
  <div class="badge" style="left:240px"><span></span></div>
  <div class="badge" style="left:394px"><span></span></div>
  <div class="badge" style="left:552px"><span></span></div>
  <div class="badge" style="left:698px"><span></span></div>
  <div class="badge" style="left:850px"><span></span></div>
  <div class="badge" style="left:1000px"><span></span></div>
</section>

<section class="video-band">
  <div class="video abs">
    <div class="video-person abs" role="img" aria-label="Video still of the institute founder speaking to camera"></div>
    <svg class="abs" style="left:258px;top:100px" width="80" height="80" viewBox="0 0 80 80">
      <circle cx="40" cy="40" r="35" fill="none" stroke="#d41a6c" stroke-width="4"/>
      <path d="M32 24 L56 40 L32 56 Z" fill="none" stroke="#d41a6c" stroke-width="4" stroke-linejoin="round"/>
    </svg>
    <p class="video-quote abs">"comfort principle"</p>
    <p class="video-text abs">You are helping your bride overcome 3 of the top 15 concerns she has.</p>
    <div class="video-bar abs"></div>
  </div>
</section>

<section class="research">
  <p class="research-title abs">Our research is not just a game changer. It is the game changer. We're rewriting the book for selling wedding cakes.</p>
  <div class="path-card" style="left:86px">
    <svg width="40" height="40" viewBox="0 0 40 40"><circle cx="20" cy="20" r="8" fill="#f8d23a"/><g stroke="#f8d23a" stroke-width="3" stroke-linecap="round"><path d="M20 3v6M20 31v6M3 20h6M31 20h6M8 8l4 4M28 28l4 4M32 8l-4 4M12 28l-4 4"/></g></svg>
    <p>I'm New to Selling Wedding Cakes…</p><div class="rule"></div><div class="cta">- Click Here -</div>
  </div>
  <div class="path-card" style="left:349px">
    <svg width="40" height="40" viewBox="0 0 40 40"><circle cx="20" cy="20" r="8" fill="#f8d23a"/><g stroke="#f8d23a" stroke-width="3" stroke-linecap="round"><path d="M20 3v6M20 31v6M3 20h6M31 20h6M8 8l4 4M28 28l4 4M32 8l-4 4M12 28l-4 4"/></g></svg>
    <p>I Want to Maintain My Sales…</p><div class="rule"></div><div class="cta">- Click Here -</div>
  </div>
  <div class="path-card" style="left:612px">
    <svg width="40" height="40" viewBox="0 0 40 40"><circle cx="20" cy="20" r="8" fill="#f8d23a"/><g stroke="#f8d23a" stroke-width="3" stroke-linecap="round"><path d="M20 3v6M20 31v6M3 20h6M31 20h6M8 8l4 4M28 28l4 4M32 8l-4 4M12 28l-4 4"/></g></svg>
    <p>I'm Eager to Boost My Sales and Profits…</p><div class="rule"></div><div class="cta">- Click Here -</div>
  </div>
  <div class="path-card" style="left:875px">
    <svg width="40" height="40" viewBox="0 0 40 40"><circle cx="20" cy="20" r="8" fill="#f8d23a"/><g stroke="#f8d23a" stroke-width="3" stroke-linecap="round"><path d="M20 3v6M20 31v6M3 20h6M31 20h6M8 8l4 4M28 28l4 4M32 8l-4 4M12 28l-4 4"/></g></svg>
    <p>I'm Ready to Dominate My Market Area…</p><div class="rule"></div><div class="cta">- Click Here -</div>
  </div>
</section>

<section class="offers">
  <div class="offer" style="left:86px">
    <div class="media" role="img" aria-label="Photo of three chefs holding a bakers award book" style="background:linear-gradient(160deg,#3a3a3a,#1a1a1a 60%,#b5162f)"></div>
    <p>Become the "a Town's Finest." You'll have an atmosphere so special, brides won't think of using anyone but you!</p>
    <div class="btn">Subscribe Now</div>
  </div>
  <div class="offer" style="left:437px">
    <div class="media" role="img" aria-label="Photo of a puzzled woman beside a large question mark" style="background:linear-gradient(140deg,#2e2e2e,#4a4a4a 55%,#8a8a8a)"></div>
    <p>Peek at a very effective psychologicalsales riddle called "The Doubt Window."</p>
    <div class="btn">Subscribe Now</div>
  </div>
  <div class="offer" style="left:789px">
    <div class="media" role="img" aria-label="Split portrait photo showing two contrasting sides of a woman" style="background:linear-gradient(90deg,#f1d6b8 0%,#e8c39c 50%,#9a9a9a 50%,#cfcfcf 100%)"></div>
    <p>Discover a sales growth secret that reveals the "Hidden Side of Your Wedding Cake Business."</p>
    <div class="btn">Subscribe Now</div>
  </div>
</section>

<section class="about">
  <div class="about-bg abs" role="img" aria-label="Soft faded photo of white wedding cake frosting"></div>
  <svg class="abs" style="left:0;top:0" width="500" height="494" viewBox="0 0 500 494">
    <polygon points="0,0 410,0 220,494 0,494" fill="#f6f6f6"/>
    <polygon points="410,0 450,0 260,494 220,494" fill="#f2b8d2"/>
    <polygon points="0,330 160,494 0,494" fill="#1fc6c2" opacity=".9"/>
  </svg>
  <div class="portrait-ring abs"><div class="portrait abs" role="img" aria-label="Portrait photo of the institute founder"></div></div>
  <div class="about-copy abs">
    <h2>Use Cutting-edge Methods Proven to Get MORE Leads, Convince MORE Brides to Choose You, Get HIGHER Prices and DOMINATE Your Competition.</h2>
    <p>Our breakthrough marketing and sales methods are possible due to the long-term studies we've conducted with 150, 000 brides over the past 12 years.</p>
    <p>From the findings, we have developed new and revolutionary marketing strategies, sales tools, and a complete transformational wedding cake sales system.</p>
    <p>But, don't take my word for it…let me "prove" the value and impact they will have on your wedding cake business.</p>
    <p class="lead">Enter Your Name and Email Address Below.</p>
    <p>Each month you'll receive our "Monthly Cake Marketing Digest." It's normally available for a $397 subscription fee. You'll receive the first year… absolutely FREE.</p>
  </div>
</section>

<section class="insider">
  <p class="insider-text abs">Join our "Baker Circle Briefing" for FREE." You'll receive the latest research secrets while learning how to use psychology for gaining a decisive advantage to market and sell your wedding cakes.</p>
  <div class="field" style="left:703px;top:47px;width:198px">First Name</div>
  <div class="field" style="left:917px;top:47px;width:197px">Last Name</div>
  <div class="field" style="left:703px;top:112px;width:411px">Your Email</div>
  <div class="btn" style="left:703px;top:180px;width:200px;height:47px;line-height:47px">Subscribe Now</div>
</section>

<section class="banner" role="img" aria-label="Dark wood plank backdrop carrying the institute name">
  <p class="banner-name">Coastal Bridal Pastry Trade Institute</p>
</section>

<footer class="site-footer">
  <div class="foot-col" style="left:86px"><h3>Marketing Solutions</h3><ul>
    <li>Unlocking the Bride Mindset Course</li><li>Individual Marketing Videos</li><li>Bundled Marketing Videos</li><li>Premier Tier Baker</li><li>Advertise For Free</li><li>Analyze Your Marketing</li><li>Priority Ladder Training</li></ul></div>
  <div class="foot-col" style="left:349px"><h3>Sales Solutions</h3><ul>
    <li>Individual Sales Tools</li><li>Bundles Sales Presentations</li><li>Monthly Baker Bulletin</li><li>Write a Wedding Cake Book</li><li>Analyze Your Sales System</li></ul></div>
  <div class="foot-col" style="left:612px"><h3>Hire Us</h3><ul>
    <li>Coaching</li><li>Consulting</li><li>Speaking</li><li>3-Day Workshops</li></ul></div>
  <div class="foot-col" style="left:877px"><h3>Partner With Us</h3><ul><li>Spread the Word</li></ul></div>
  <div class="foot-brand abs"><span class="brand-dot" style="width:18px;height:18px"></span>Coastal Bridal Pastry Trade Institute</div>
  <div class="foot-rule abs"></div>
  <p class="copyright abs">Coastal Bridal Pastry Trade Institute © 2019 &nbsp;|&nbsp; All Rights Reserved.</p>
</footer>

</body>
</html>
```